Vina Solvara

Solvara embodies the purity and intensity of Chile’s cold coastal terroir. The sleek white label and bold X logo reflect the stark beauty and unrelenting nature of these extreme winemaking conditions. Crisp, vibrant, and refreshingly bold, Solvara is a tribute to the wild energy of the Pacific winds and the cool embrace of the coastal valleys—a wine for those who seek purity and perfection in every sip. We would like to have a simple design focusing o the X, we try some option see attach but we are no satisfied is not enaguh eyes catching
Updates

Please create a mysterious, enigmatic label based on the typography and logo attached to the project. We need at least, at the entry level, five varietal products such as Carménère, Cabernet Sauvignon, Merlot, Chardonnay, and Malbec. Later, we would like to add more premium products, like a Reserva, a Special Reserva, or a Limited Edition. The design should be flexible and easily adaptable to accommodate various products while maintaining the same overall aesthetic.

I upload some wines label with printing technic we would like to use on our label, please incorporate this into your design

Project Brief – Large-Scale Brand Label Design
We are developing a new large-scale brand with a structured range of wines. Below are the key design elements and specifications for the labels:

Pinot Noir, Chardonnay, Syrah (Burgundy bottle shape – must include "Special Reserve" on the label)
General Label Guidelines
Year: Only mention "2024" (do not include the word “vintage”).
Capsules: Use standard-colored capsules only (no branding).
Label Design:
Focus on the label itself; bottle and background are irrelevant.
We can consider a wraparound label, but space must be reserved for back-label information.
Please refer to www.pelnorth-wines.example for brand coherence. Let us know if further details are needed.

Target Market(s)

peopels who looking for simple design but strinking with the X . THe X could be like a painting brush somehting which make it look artistic

Industry/Entity Type

Wines producer

Font styles to use
Decorative
Script
Other font styles liked:
• the X would be nice if it look like he is Brush from a painter

Colors
0054AA
0677BA
7BADD7
CADEEF
E8F1F8
FFF300
FFF600
FEFA6F
FFFEC7
FFFEE8
EB3D1F
EC4F4E
F09395
F8D3D4
FCEDEE

Requirements
Must have
• We need to indicate the varietals Cabernet Sauvignon, the vintage 2024, the region DO Central Valley
Nice to have
• option on a burgendy bottle for chardonnay and pinot noir and option on bordeau bottle for Cabernet sauvignon and Merlot, We will need a large serie of 5 entrance lebvel (4 red one white) 2 reserve, 2 special reserve, 2 Limited

```html
<!DOCTYPE html>
<html lang="en">
<head>
<meta charset="utf-8">
<title>Solvara Chardonnay – Label</title>
<link rel="stylesheet" href="https://fonts.googleapis.com/css2?family=Montserrat:wght@700&family=Forum&display=swap">
<style>
  :root {
    --ink: #3b2a22;
    --paper: #ffffff;
    --amber-deep: #a4461d;
    --amber: #e3851c;
    --gold: #f4b42a;
    --sun: #f8d23e;
    --cream: #efe3c8;
  }
  * { margin: 0; padding: 0; box-sizing: border-box; }
  html, body {
    width: 1051px;
    height: 1200px;
    overflow: hidden;
    background: var(--paper);
  }
  .label {
    position: relative;
    width: 1051px;
    height: 1200px;
    overflow: hidden;
  }
  .label__art {
    position: absolute;
    inset: 0;
    width: 1051px;
    height: 1200px;
  }
  .label__text {
    position: absolute;
    left: 0;
    width: 1051px;
    text-align: center;
    color: var(--ink);
    white-space: nowrap;
  }
  .brand-name {
    top: 572px;
    padding-left: 36px;
    font-family: "Montserrat", sans-serif;
    font-weight: 700;
    font-size: 104px;
    line-height: 1;
    letter-spacing: 1px;
  }
  .varietal {
    top: 702px;
    padding-left: 36px;
    font-family: "Forum", serif;
    font-size: 68px;
    line-height: 1;
    letter-spacing: 2px;
  }
  .divider {
    position: absolute;
    top: 857px;
    left: 345px;
    width: 373px;
    height: 2px;
    background: var(--ink);
  }
  .appellation {
    top: 872px;
    padding-left: 36px;
    font-family: "Forum", serif;
    font-size: 30px;
    line-height: 1;
    letter-spacing: 1px;
  }
  .year {
    top: 914px;
    padding-left: 36px;
    font-family: "Forum", serif;
    font-size: 30px;
    line-height: 1;
  }
</style>
</head>
<body>
  <main class="label">
    <svg class="label__art" viewBox="0 0 1051 1200" xmlns="http://www.w3.org/2000/svg">
      <defs>
        <linearGradient id="wave-tones" x1="0" y1="0" x2="1" y2="1">
          <stop offset="0" stop-color="var(--gold)"/>
          <stop offset="0.3" stop-color="var(--amber)"/>
          <stop offset="0.55" stop-color="var(--sun)"/>
          <stop offset="0.8" stop-color="var(--amber)"/>
          <stop offset="1" stop-color="var(--amber-deep)"/>
        </linearGradient>
      </defs>
      <rect class="wave-field" width="1051" height="1200" fill="url(#wave-tones)"
            role="img" aria-label="Painted illustration of swirling golden and amber ocean waves framing the label"/>
      <path class="text-panel" fill="var(--paper)"
            d="M230 0 L820 0 L790 300 C780 420 835 470 835 560 L835 880 C835 960 790 1000 700 1010 L350 1010 C260 1000 215 960 215 880 L215 560 C215 470 265 420 255 300 Z"/>
      <circle class="brand-mark" cx="525" cy="265" r="215" fill="var(--amber-deep)"
              role="img" aria-label="Brand mark area"/>
    </svg>

    <h1 class="label__text brand-name">SOLVARA</h1>
    <p class="label__text varietal">CHARDONNAY</p>
    <div class="divider"></div>
    <p class="label__text appellation">DO CENTRAL VALLEY</p>
    <p class="label__text year">2024</p>
  </main>
</body>
</html>
```